Events floral designer business needs a logo design

I need a logo design for my floral design business called tender thorns.
i am inspired by nature and the simplicity of its beauty, whilst upcycling and recycling materials to reduce waste and impact on our environment.
I would like the design to be printed on recycled brown cardboard so i would like a simple but striking design of a bold black ivy vine or gnarly magnolia or tree branch with lower case old school type writer font.

Target Market(s)

Anyone requiring floral additions for their event

Industry/Entity Type

Business

Contact Information for Business Card

mara hollis
floral designer/creator
0418657203
mara@tenderthorns.com
tenderthorns.com

Font styles to use
Other font styles liked:
• lower case type writer

Colors
000000

Requirements
Must have
• simplicity but boldness
• Black typewriter font and bold picture with my details
Nice to have
• as above
Should not have
• colour

```html
<!DOCTYPE html>
<html lang="en">
<head>
<meta charset="utf-8">
<title>tender thorns — business card</title>
<link rel="stylesheet" href="https://fonts.googleapis.com/css2?family=Special+Elite&display=swap">
<style>
  :root {
    --backdrop: #1b1b1b;
    --kraft: #a88f6c;
    --kraft-light: #b39b78;
    --kraft-dark: #967d5c;
    --ink: #141210;
    --mark: #3a3631;
  }
  * { margin: 0; padding: 0; box-sizing: border-box; }
  html, body {
    width: 1200px;
    height: 1200px;
    overflow: hidden;
    background: var(--backdrop);
  }
  .stage {
    width: 1200px;
    height: 1200px;
    display: flex;
    align-items: center;
    justify-content: center;
  }
  .business-card {
    position: relative;
    width: 1000px;
    height: 630px;
    border-radius: 44px;
    background:
      radial-gradient(ellipse at 30% 35%, var(--kraft-light) 0%, transparent 60%),
      radial-gradient(ellipse at 75% 80%, var(--kraft-dark) 0%, transparent 55%),
      var(--kraft);
    font-family: "Special Elite", "Courier New", monospace;
    color: var(--ink);
    text-align: center;
  }
  .brand-mark {
    position: absolute;
    left: 50%;
    top: 80px;
    transform: translateX(-50%);
  }
  .brand-name {
    position: absolute;
    top: 240px;
    width: 100%;
    font-size: 36px;
    letter-spacing: 0.14em;
    text-transform: lowercase;
  }
  .divider {
    position: absolute;
    top: 320px;
    left: 50%;
    width: 190px;
    height: 2px;
    margin-left: -95px;
    background: var(--ink);
  }
  .contact {
    position: absolute;
    top: 366px;
    width: 100%;
    list-style: none;
    font-size: 27px;
    line-height: 40px;
    letter-spacing: 0.06em;
  }
  .contact .person {
    font-size: 34px;
    line-height: 46px;
    letter-spacing: 0.1em;
  }
</style>
</head>
<body>
  <main class="stage">
    <section class="business-card">
      <svg class="brand-mark" width="120" height="120" viewBox="0 0 120 120" aria-hidden="true">
        <circle cx="60" cy="60" r="52" fill="var(--mark)"/>
      </svg>
      <h1 class="brand-name">tender thorns</h1>
      <div class="divider"></div>
      <ul class="contact">
        <li class="person">Mara Hollis</li>
        <li>Floral designer/creator</li>
        <li>0418657203</li>
        <li>mara@tenderthorns.com</li>
        <li>tenderthorns.com</li>
      </ul>
    </section>
  </main>
</body>
</html>
```